Velmoro Cabinets Letter Head and Email Signature

Hi
I would love a design package for a letterhead, email signature, even update my business card if you like if you can come up with a great idea for my new high end cabinet shop. Velmoro Cabinets brings timeless craftsmanship to modern interiors, specializing in high end, custom cabinetry designed for architects and interior designers.

Target Market(s)

high end, luxury market

Industry/Entity Type

cabinet making

Requirements
Must have
• my colours of logo as the theme

```html
<!DOCTYPE html>
<html lang="en">
<head>
<meta charset="utf-8">
<title>Velmoro Cabinets – Stationery</title>
<link href="https://fonts.googleapis.com/css2?family=Montserrat:ital,wght@0,400;0,500;0,700;1,800&family=Lato:wght@400&display=swap" rel="stylesheet">
<style>
  :root{
    --brand-green:#4a7c47;
    --ink:#1b1b1b;
    --paper:#ffffff;
    --card-dark:#1a1a1a;
    --emboss:#262626;
    --stage:#adadad;
    --body-text:#3a3a3a;
  }
  *{margin:0;padding:0;box-sizing:border-box}
  html,body{width:1200px;height:795px;overflow:hidden}
  body{background:var(--stage);position:relative;font-family:'Montserrat',sans-serif;color:var(--ink)}

  .presentation-title{
    position:absolute;left:330px;top:18px;width:680px;text-align:center;
    font-family:'Montserrat',sans-serif;font-weight:800;font-style:italic;
    font-size:62px;line-height:76px;color:var(--brand-green);letter-spacing:-1px;
  }

  /* Brand wordmark: square + stacked name, one colour, one weight */
  .brand-name{
    display:flex;align-items:center;
    font-family:'Montserrat',sans-serif;font-weight:500;color:var(--brand-green);white-space:nowrap;
  }
  .brand-name .brand-square{background:var(--brand-green);flex:none}
  .brand-words{display:flex;flex-direction:column}

  /* Letterhead */
  .letterhead{
    position:absolute;left:160px;top:137px;width:368px;height:521px;
    background:var(--paper);box-shadow:-6px 6px 10px rgba(0,0,0,.35);overflow:hidden;
  }
  .letterhead .brand-name{position:absolute;left:35px;top:21px;gap:10px;font-size:15px;line-height:16px}
  .letterhead .brand-name .brand-square{width:30px;height:30px}
  .lh-contact{
    position:absolute;left:226px;top:24px;border-left:1px solid var(--brand-green);
    padding-left:9px;height:25px;
  }
  .lh-contact li{font-size:6.4px;line-height:9px;list-style:none;display:flex;align-items:center;gap:3px;color:var(--ink)}
  .icon{flex:none;fill:var(--brand-green)}
  .lh-contact .icon{width:5px;height:5px}
  .recipient{position:absolute;left:35px;top:122px;font-family:'Lato',sans-serif;color:var(--body-text);font-style:normal}
  .recipient .recipient-name{font-size:7px;line-height:10px}
  .recipient .recipient-line{font-size:5px;line-height:9px}
  .letter-body{
    position:absolute;left:35px;top:184px;width:298px;
    font-family:'Lato',sans-serif;font-size:5.1px;line-height:9.1px;color:var(--body-text);text-align:justify;
  }
  .letter-body p{margin-bottom:7.6px}
  .sign-off{position:absolute;left:35px;top:385px;font-family:'Lato',sans-serif;color:var(--body-text)}
  .sign-off .closing{font-size:5.8px;line-height:8px}
  .signature-mark{width:44px;height:12px;margin:5px 0 3px;background:linear-gradient(90deg,#e4e4e4,#d6d6d6);border-radius:2px}
  .sign-off .signer{font-size:7px;line-height:9px}
  .footer-band{position:absolute;bottom:0;height:14px}
  .footer-band.green{left:0;width:190px;background:var(--brand-green);clip-path:polygon(0 0,182px 0,190px 14px,0 14px)}
  .footer-band.black{right:0;width:60px;background:#000;clip-path:polygon(8px 0,60px 0,60px 14px,0 14px)}

  /* Email signature */
  .email-signature{
    position:absolute;left:587px;top:109px;width:454px;height:164px;
    background:var(--paper);box-shadow:-6px 6px 10px rgba(0,0,0,.35);
  }
  .email-signature .brand-name{position:absolute;left:40px;top:57px;gap:14px;font-size:24px;line-height:25px}
  .email-signature .brand-name .brand-square{width:46px;height:46px}
  .divider{position:absolute;width:1px;background:var(--brand-green)}
  .email-signature .divider{left:226px;top:37px;height:90px}
  .person{position:absolute}
  .person-name{font-weight:700;color:var(--brand-green)}
  .person-role{font-weight:400}
  .contact-list li{list-style:none;display:flex;align-items:center;gap:5px}
  .email-signature .person{left:250px;top:33px}
  .email-signature .person-name{font-size:18.5px;line-height:22px}
  .email-signature .person-role{font-size:11px;line-height:14px;color:#2a2a2a}
  .email-signature .contact-list{margin-top:14px}
  .email-signature .contact-list li{font-size:11.2px;line-height:16px;color:#2a2a2a}
  .email-signature .icon{width:9px;height:9px}

  /* Business cards */
  .business-card{position:absolute;left:587px;width:313px;height:179px;background:var(--card-dark);border-radius:12px}
  .business-card.front{top:301px}
  .business-card.back{top:508px}
  .business-card.front .brand-name{position:absolute;left:16px;top:71px;gap:10px;font-size:17px;line-height:18px}
  .business-card.front .brand-name .brand-square{width:34px;height:34px}
  .business-card.front .divider{left:156px;top:54px;height:72px}
  .business-card.front .person{left:167px;top:51px}
  .business-card.front .person-name{font-size:15px;line-height:18px}
  .business-card.front .person-role{font-size:8.6px;line-height:11px;color:#fff}
  .business-card.front .contact-list{margin-top:11px}
  .business-card.front .contact-list li{font-size:8.6px;line-height:12.6px;color:#fff;gap:3px}
  .business-card.front .icon{width:7px;height:7px}
  .business-card.back .brand-name{
    position:absolute;left:0;top:0;width:313px;height:179px;justify-content:center;gap:16px;
    font-size:32px;line-height:34px;color:var(--emboss);
  }
  .business-card.back .brand-name .brand-square{width:64px;height:64px;background:var(--emboss)}
</style>
</head>
<body>

<h1 class="presentation-title">Version -2 (Updated)</h1>

<svg width="0" height="0" style="position:absolute">
  <symbol id="icon-phone" viewBox="0 0 10 10"><path d="M1 3.2C1 2 2.6 1.3 5 1.3S9 2 9 3.2L7.6 3.9 6.8 3V2.6H3.2V3L2.4 3.9ZM3 4.2h4l1.5 4.4H1.5Z"/></symbol>
  <symbol id="icon-mail" viewBox="0 0 10 10"><path d="M0.5 2h9v6h-9Zm1 1v0.3L5 5.6 8.5 3.3V3ZM1.5 4.5V7h7V4.5L5 6.8Z"/></symbol>
  <symbol id="icon-social" viewBox="0 0 10 10"><circle cx="5" cy="5" r="4"/></symbol>
</svg>

<section class="letterhead">
  <div class="brand-name"><span class="brand-square"></span><span class="brand-words"><span>Velmoro</span><span>Cabinets</span></span></div>
  <ul class="lh-contact">
    <li><svg class="icon"><use href="#icon-phone"/></svg>0412558301</li>
    <li><svg class="icon"><use href="#icon-mail"/></svg>info@velmorocabinets.com.au</li>
    <li><svg class="icon"><use href="#icon-social"/></svg>@velmoro.cabinets</li>
  </ul>

  <address class="recipient">
    <div class="recipient-name">HARRIET COLBY</div>
    <div class="recipient-line">Chief Exective Officer</div>
    <div class="recipient-line">City/State, Zip Code</div>
  </address>

  <div class="letter-body">
    <p>Thank you for considering Velmoro Cabinets for your upcoming residence. Our workshop builds every piece by hand, pairing solid timber with precise joinery and finishes chosen to suit the architecture of each room. We work closely with architects and interior designers from the first sketch to final installation, so that proportions, hardware and materials sit naturally within the space. Attached you will find a summary of the scope we discussed, together with timber samples, finish options and an outline of the build schedule for the kitchen, library and principal dressing room.</p>
    <p>Each cabinet is drawn to measure in our studio before any timber is cut. Once the drawings are approved, our craftsmen prepare the carcasses, doors and drawer fronts, and every surface is sanded and sealed by hand. We invite you to visit the workshop at any stage to review progress, handle the finishes and confirm the final details with our team.</p>
    <p>Installation is carried out by the same people who built your cabinetry, ensuring that every line is level and every door closes quietly. Should you have any questions about the proposal, the materials or the timing, please contact me directly. We look forward to creating a lasting piece of craftsmanship for your home.</p>
  </div>

  <div class="sign-off">
    <div class="closing">Sincerely,</div>
    <div class="signature-mark" role="img" aria-label="Handwritten signature"></div>
    <div class="signer">Dorian Kessler</div>
  </div>

  <div class="footer-band green"></div>
  <div class="footer-band black"></div>
</section>

<section class="email-signature">
  <div class="brand-name"><span class="brand-square"></span><span class="brand-words"><span>Velmoro</span><span>Cabinets</span></span></div>
  <div class="divider"></div>
  <div class="person">
    <div class="person-name">Dorian Kessler</div>
    <div class="person-role">Director Craftsman</div>
    <ul class="contact-list">
      <li><svg class="icon"><use href="#icon-phone"/></svg>0412558301</li>
      <li><svg class="icon"><use href="#icon-mail"/></svg>info@velmorocabinets.com.au</li>
      <li><svg class="icon"><use href="#icon-social"/></svg>@velmoro.cabinets</li>
    </ul>
  </div>
</section>

<section class="business-card front">
  <div class="brand-name"><span class="brand-square"></span><span class="brand-words"><span>Velmoro</span><span>Cabinets</span></span></div>
  <div class="divider"></div>
  <div class="person">
    <div class="person-name">Dorian Kessler</div>
    <div class="person-role">Director Craftsman</div>
    <ul class="contact-list">
      <li><svg class="icon"><use href="#icon-phone"/></svg>0412558301</li>
      <li><svg class="icon"><use href="#icon-mail"/></svg>info@velmorocabinets.com.au</li>
      <li><svg class="icon"><use href="#icon-social"/></svg>@velmoro.cabinets</li>
    </ul>
  </div>
</section>

<section class="business-card back">
  <div class="brand-name"><span class="brand-square"></span><span class="brand-words"><span>Velmoro</span><span>Cabinets</span></span></div>
</section>

</body>
</html>
```